Wordpress Identity for Innovation Firm

Copper Lantern Partners is an innovation and investment firm based in Los Angeles.

We are seeking a designer that can help create our company identity and Wordpress site.

The attached Design Brief provides more details.

Designers Responsibility:

1) Company Identity

The designer will create the company identity.
Attached is a file that contains a type font that I like a lot.
No logo design is required.

The Copper Lantern Partners type font should become the company identity.
The attached document provides an overview of company type font identities that we like.

2) Wordpress Theme & Design

The designer will select existing Wordpress Themes that meet our design desires, and present them as part of the design proposal.

We will make our selection based on the selected Wordpress Theme(s), which the designer will creatively adapt with the new company identity.

Target Market(s)

We anticipate the website being mostly accessed by the US, Canada and European countries.

Our target audience includes the following:

• Corporations, companies, startups, non-profits
• Banks, venture capital, private equity, investors
• Incubators, accelerators, innovation clusters, research labs, universities
• Ad agencies, marketing agencies, digital agencies, media, press

Industry/Entity Type

Investment

Number of Pages Required

1 page

Font styles to use
Sans Serif
Other font styles liked:
• See attached design brief materials. The Font will represent the brand identity!

Requirements
Must have
• The ability to scroll through information top to bottom is important to us.
• This is in line with today's Wordpress themes.
• The website must be able to function across devices (desktop, tablet, phone).
• The top 5 web browsers and platforms (Mac/PC/Android/iOS)
• Contact us link or information field
Nice to have
• It would be nice to have a moving image in the background, such as:
• https://drifttrial.sitehatch.com
• The Wordpress theme of the moving image or video should be relevant to our overall Technology Innovation theme.
• Key words:
• Technology Innovation
• Digital
• Business
• Transportation
• Advanced Vehicles (auto, boat, airplane, rail, space)
• Space
• Venture Capital
• Investing
Should not have
• eCommerce

```html
<!DOCTYPE html>
<html lang="en">
<head>
<meta charset="utf-8">
<title>Copper Lantern Partners</title>
<link href="https://fonts.googleapis.com/css2?family=Roboto:wght@300;400;500&display=swap" rel="stylesheet">
<style>
:root{
  --blue:#1b8fe6;
  --blue-deep:#0f6fd0;
  --ink:#2b2f33;
  --muted:#7b8086;
  --panel:#efefef;
  --white:#ffffff;
  --footer:#2a2d31;
  --hero-dark:#1d2226;
}
*{margin:0;padding:0;box-sizing:border-box}
html,body{width:1200px;height:2592px;overflow:hidden}
body{font-family:"Roboto",sans-serif;color:var(--ink);background:var(--white);font-weight:300}
.hero{position:relative;height:592px;color:var(--white);text-align:center}
.hero-media{position:absolute;inset:0;background:radial-gradient(ellipse at 75% 25%,#8b9499 0%,#4a5358 35%,var(--hero-dark) 80%)}
.nav{position:absolute;top:0;left:0;right:0;height:56px;display:flex;align-items:center;justify-content:space-between;padding:0 56px}
.brand{font-size:30px;font-weight:500;color:var(--white)}
.menu{display:flex;gap:34px;font-size:12px;font-weight:400;letter-spacing:1px}
.menu a{color:var(--white);text-decoration:none;padding:18px 12px}
.menu a.active{background:var(--blue)}
.hero-title{position:relative;padding-top:252px;font-size:50px;font-weight:300;letter-spacing:1px}
.hero-text{position:relative;width:820px;margin:30px auto 0;font-size:15px;line-height:26px;opacity:.9}
.btn{display:inline-block;background:var(--blue);color:var(--white);font-size:12px;font-weight:500;letter-spacing:1px;padding:14px 34px;text-decoration:none}
.hero .btn{position:relative;margin-top:94px}
.bring{height:768px;background:var(--panel);text-align:center;padding-top:70px}
.section-title{font-size:38px;font-weight:300;letter-spacing:1px;color:var(--ink)}
.features{display:flex;justify-content:center;gap:60px;margin-top:76px}
.feature{width:300px}
.feature svg{display:block;margin:0 auto}
.feature h3{font-size:15px;font-weight:400;letter-spacing:.5px;margin-top:40px}
.feature p{font-size:13px;line-height:22px;color:var(--muted);margin-top:18px}
.projects{height:720px;text-align:center;padding-top:44px}
.projects-lead{width:860px;margin:22px auto 0;font-size:15px;line-height:26px;color:var(--blue)}
.grid{display:grid;grid-template-columns:repeat(4,300px);grid-auto-rows:232px;margin-top:40px}
.tile{position:relative;display:flex;flex-direction:column;align-items:center;justify-content:center;color:var(--white);font-size:13px;font-weight:400}
.tile-badge{width:44px;height:44px;border-radius:50%;background:var(--blue);margin-bottom:10px}
.projects .btn{margin-top:44px}
.contact{height:448px;background:linear-gradient(135deg,#1f8ff0 0%,var(--blue-deep) 60%,#0b5fbf 100%);color:var(--white);padding:40px 60px 0}
.contact .section-title{color:var(--white);text-align:center}
.form-row{display:flex;gap:36px;margin-top:30px}
.field{flex:1;display:flex;flex-direction:column}
.field label{font-size:12px;font-weight:400;margin-bottom:6px}
.field span{height:40px;background:var(--white)}
.field.wide{margin-top:20px}
.field.wide span{height:104px}
.send{text-align:center;margin-top:22px}
.send .btn{background:var(--hero-dark)}
.footer{height:64px;background:var(--footer);display:flex;align-items:center;justify-content:space-between;padding:0 60px;color:#9aa0a6;font-size:12px}
.social{display:flex;gap:10px}
.social span{width:22px;height:22px;border-radius:50%;background:#7d838a}
</style>
</head>
<body>
<header class="hero">
  <div class="hero-media" role="img" aria-label="Dark photograph of hanging light bulbs with one bright bulb"></div>
  <nav class="nav">
    <div class="brand">Copper</div>
    <div class="menu"><a class="active">HOME</a><a>ABOUT</a><a>OUR PROJECTS</a><a>BLOG</a><a>CONTACT</a></div>
  </nav>
  <h1 class="hero-title">COPPER LANTERN PARTNERS</h1>
  <p class="hero-text">Copper Lantern Partners helps corporations build sustainable competitive advantage through superior innovation and operating performance and has the ability to provide all-round partnership models.</p>
  <a class="btn">&#9679;&nbsp; READ MORE</a>
</header>

<section class="bring">
  <h2 class="section-title">WHAT WE BRING TO THE TABLE</h2>
  <div class="features">
    <div class="feature">
      <svg width="104" height="116" viewBox="0 0 104 116"><polygon points="52,3 100,30 100,86 52,113 4,86 4,30" fill="none" stroke="#1b8fe6" stroke-width="3"/><rect x="33" y="38" width="38" height="40" fill="none" stroke="#1b8fe6" stroke-width="3"/><rect x="40" y="60" width="6" height="12" fill="#1b8fe6"/><rect x="49" y="52" width="6" height="20" fill="#1b8fe6"/><rect x="58" y="45" width="6" height="27" fill="#1b8fe6"/></svg>
      <h3>WE BUILD NEW BUSINESS</h3>
      <p>Today's age of innovation is driven by the accelerating evolution of technology and data, which has fundamentally changed consumer behavior. As a result, companies are faced with accelerating pressure to put innovation at the center of their business. Our team brings startups to our partners.</p>
    </div>
    <div class="feature">
      <svg width="104" height="116" viewBox="0 0 104 116"><polygon points="52,3 100,30 100,86 52,113 4,86 4,30" fill="none" stroke="#1b8fe6" stroke-width="3"/><polygon points="52,34 76,58 52,82 28,58" fill="none" stroke="#1b8fe6" stroke-width="3"/><polygon points="52,46 64,58 52,70 40,58" fill="#1b8fe6"/></svg>
      <h3>WE BUILD PARTNERSHIPS</h3>
      <p>We introduce new ways of thinking and doing in order to create gains in changing competitive environments. Most large companies are structured to maximize efficiency, so we bring entrepreneurial spirit and fresh models that help them move faster and grow beyond the core.</p>
    </div>
    <div class="feature">
      <svg width="104" height="116" viewBox="0 0 104 116"><polygon points="52,3 100,30 100,86 52,113 4,86 4,30" fill="none" stroke="#1b8fe6" stroke-width="3"/><rect x="32" y="46" width="28" height="28" fill="none" stroke="#1b8fe6" stroke-width="3"/><rect x="44" y="36" width="28" height="28" fill="none" stroke="#1b8fe6" stroke-width="3"/></svg>
      <h3>WE CULTIVATE COLLABORATION</h3>
      <p>We cultivate collaboration by building ecosystems and solving complex technological challenges and pain points. Our key goal is to drive growth for our partners and support them to stay relevant in the digital era, leveraging their existing assets and becoming disruptors.</p>
    </div>
  </div>
</section>

<section class="projects">
  <h2 class="section-title">OUR PROJECTS</h2>
  <p class="projects-lead">Copper Lantern Partners is an entrepreneurial organization that cares about outcomes. We fundamentally believe that the greatest success in innovation originates from entrepreneurs — not consultants.</p>
  <div class="grid">
    <div class="tile" role="img" aria-label="Aerial drone over a city" style="background:linear-gradient(160deg,#9fb4c2,#4d5f6b)"></div>
    <div class="tile" role="img" aria-label="Technology innovation project with glowing blue lights" style="background:linear-gradient(160deg,#2a3c55,#0e1726)"><span class="tile-badge"></span>Technology Innovation</div>
    <div class="tile" role="img" aria-label="Glowing sphere in a dark room" style="background:radial-gradient(circle at 40% 50%,#c9d7e6,#233244 60%,#0b1018)"></div>
    <div class="tile" role="img" aria-label="Microscope in a laboratory" style="background:linear-gradient(160deg,#e6e9ee,#9aa3ad)"></div>
    <div class="tile" role="img" aria-label="Person wearing headset" style="background:linear-gradient(160deg,#5d6a78,#1f2a36)"></div>
    <div class="tile" role="img" aria-label="Green plant sprouts" style="background:linear-gradient(160deg,#bfe2d3,#3d8f74)"></div>
    <div class="tile" role="img" aria-label="Hand holding a glowing device" style="background:linear-gradient(160deg,#4a5866,#151c24)"></div>
    <div class="tile" role="img" aria-label="Rocket launch at sunset" style="background:linear-gradient(180deg,#f3c27a,#c46b2c 60%,#3a2a24)"></div>
  </div>
  <a class="btn">&#8635;&nbsp; VIEW MORE</a>
</section>

<section class="contact">
  <h2 class="section-title">CONTACT US</h2>
  <div class="form-row">
    <div class="field"><label>Your Name (required)</label><span></span></div>
    <div class="field"><label>Your Email (required)</label><span></span></div>
    <div class="field"><label>Subject</label><span></span></div>
  </div>
  <div class="field wide"><label>Tell us about your project</label><span></span></div>
  <div class="send"><a class="btn">&#10148;&nbsp; SEND MESSAGE</a></div>
</section>

<footer class="footer">
  <div>© 2015 Copper Lantern Partners</div>
  <div class="social"><span></span><span></span><span></span><span></span><span></span><span></span></div>
</footer>
</body>
</html>
```